Flyer-Design für Hypnose
Zielgruppe
Hypnose
Aufgabenstellung
Text Vorder- und Rückseite siehe Anlage
Auf der Vorderseite Foto und Logo (auch in der Anlage)
Farbgestaltung passend zu den Logofarben
Das Design soll kreativ und freundlich sein

```html
<!DOCTYPE html>
<html lang="de">
<head>
<meta charset="utf-8">
<title>Seelenruh Hypnose – Flyer</title>
<link href="https://fonts.googleapis.com/css2?family=Hind:wght@400;500&family=Alegreya+Sans:wght@400;500;700&family=Merriweather:wght@400;700&family=Kaushan+Script&display=swap" rel="stylesheet">
<style>
  :root{
    --bg:#f2f2f4;
    --white:#ffffff;
    --coral:#ef6a3c;
    --red:#e8472b;
    --peach:#f6b699;
    --quote:#fde0d2;
    --yellow:#f1ec98;
    --yellow-text:#ece382;
    --blue:#a8c7ea;
    --ink:#1b1b1b;
  }
  *{margin:0;padding:0;box-sizing:border-box}
  html,body{width:1200px;height:1200px;overflow:hidden;background:var(--bg)}
  .canvas{position:relative;width:1200px;height:1200px}
  .panel{position:absolute;top:104px;width:467px;height:991px;background:var(--white);overflow:hidden}
  .panel--front{left:121px}
  .panel--back{left:612px}

  /* front */
  .brand{position:absolute;left:0;top:140px;width:265px;text-align:center;font-family:"Alegreya Sans",sans-serif;color:var(--coral)}
  .brand__mark{display:block;width:14px;height:14px;border-radius:50%;background:var(--coral);margin:0 auto 10px}
  .brand__name{font-size:40px;font-weight:700;line-height:1}
  .brand__sub{display:flex;align-items:center;justify-content:center;gap:12px;font-size:18px;letter-spacing:4px;margin-top:6px}
  .brand__sub::before,.brand__sub::after{content:"";width:40px;height:1.5px;background:var(--coral)}
  .portrait{position:absolute;left:285px;top:200px;width:182px;height:791px;border-radius:90px 0 0 0;background:linear-gradient(180deg,#bdb9b1 0%,#e6c8b6 40%,#f7bba8 70%,#f1a090 100%)}
  .name-band{position:absolute;left:0;top:621px;width:339px;height:63px;background:var(--peach);border-radius:0 32px 32px 0;text-align:center;font-family:"Merriweather",serif;color:var(--white);font-size:16px;line-height:23px;padding-top:9px}
  .contact{position:absolute;left:31px;font-family:"Alegreya Sans",sans-serif;color:var(--coral)}
  .contact--phone{top:706px;display:flex;align-items:center;gap:12px;font-family:"Merriweather",serif;font-weight:700;font-size:27px}
  .contact--mail{top:756px;font-size:18px}
  .contact__rule{position:absolute;left:31px;top:792px;width:123px;height:1.5px;background:var(--coral)}
  .contact--addr{top:802px;font-size:18px;line-height:23px}
  .front-wave{position:absolute;left:0;bottom:0;width:467px;height:100px}
  .front-web{position:absolute;left:0;width:467px;bottom:30px;text-align:center;font-family:"Merriweather",serif;font-weight:700;font-size:22px;color:var(--white);padding-left:18px}

  /* back */
  .landscape{position:absolute;left:0;top:0;width:467px;height:203px;background:linear-gradient(180deg,#c9dde0 0%,#8fa68f 40%,#55705a 65%,#8fb0b3 100%)}
  .pill{position:absolute;left:68px;width:326px;height:31px;background:var(--yellow);border-radius:8px;font-family:"Merriweather",serif;font-weight:700;font-size:17px;color:var(--white);text-align:center;line-height:31px}
  .pill--one{top:188px}
  .pill--two{top:552px}
  .copy{position:absolute;left:0;width:467px;text-align:center;font-family:"Hind",sans-serif;font-size:17px;line-height:23.3px;color:var(--ink);white-space:nowrap}
  .copy--intro{top:238px}
  .copy--about{top:605px}
  .topics{position:absolute;left:0;top:352px;width:467px;text-align:center;font-family:"Hind",sans-serif;font-size:17px;line-height:25px;white-space:nowrap}
  .topics span{margin:0 4px}
  .t-blue{color:var(--blue)}
  .t-yellow{color:var(--yellow-text)}
  .t-red{color:var(--red)}
  .back-wave{position:absolute;left:0;bottom:0;width:467px;height:220px}
  .quote{position:absolute;left:0;top:818px;width:467px;text-align:center;font-family:"Kaushan Script",cursive;font-size:26px;line-height:38px;color:var(--quote)}
</style>
</head>
<body>
<div class="canvas">

  <section class="panel panel--front">
    <div class="brand">
      <span class="brand__mark"></span>
      <div class="brand__name">seelenruh</div>
      <div class="brand__sub">HYPNOSE</div>
    </div>

    <div class="portrait" role="img" aria-label="Porträtfoto der Hypnosetrainerin"></div>

    <div class="name-band">Mag. Daniela Kelbritor, BEd MSc<br>Diplomierte Hypnosetrainerin</div>

    <div class="contact contact--phone">
      <svg width="26" height="26" viewBox="0 0 24 24" aria-hidden="true"><path fill="#ef6a3c" d="M6.6 10.8a15 15 0 0 0 6.6 6.6l2.2-2.2a1 1 0 0 1 1-.25 11.4 11.4 0 0 0 3.6.57 1 1 0 0 1 1 1V20a1 1 0 0 1-1 1A17 17 0 0 1 3 4a1 1 0 0 1 1-1h3.5a1 1 0 0 1 1 1c0 1.25.2 2.45.57 3.57a1 1 0 0 1-.25 1z"/><path d="M14 2.5a8 8 0 0 1 7.5 7.5M14 6a4.5 4.5 0 0 1 4 4" stroke="#ef6a3c" stroke-width="1.6" fill="none"/></svg>
      0670/5550123
    </div>
    <div class="contact contact--mail">info@seelenruh-hypnose.at</div>
    <div class="contact__rule"></div>
    <div class="contact contact--addr">Am Lindenhang 14-16<br>2360 Talheim</div>

    <svg class="front-wave" viewBox="0 0 467 100" preserveAspectRatio="none" aria-hidden="true">
      <path d="M0 20 Q230 -10 467 12 L467 100 L0 100 Z" fill="#f6b699"/>
    </svg>
    <div class="front-web">www.seelenruh-hypnose.at</div>
  </section>

  <section class="panel panel--back">
    <div class="landscape" role="img" aria-label="Foto: Person sitzt auf einem Holzsteg an einem Bergsee"></div>
    <div class="pill pill--one">Wie Hypnose Ihr Leben verändert</div>

    <p class="copy copy--intro">Hypnose ist eine wunderbare Möglichkeit, das eigene<br>Leben zu verbessern. Die Anwendungsbereiche sind<br>unglaublich vielfältig – wenn einer der folgenden<br>Punkte auf Sie zutrifft, sind Sie bei mir richtig:</p>

    <div class="topics">
      <span class="t-blue">Trauer</span><span class="t-yellow">Erschöpfung/Überforderung</span><br>
      <span class="t-red">Unsicherheit in Menschenmengen</span><span class="t-blue">Platzangst</span><br>
      <span class="t-blue">Höhenangst</span><span class="t-yellow">Wunsch mit dem Rauchen aufzuhören</span><br>
      <span class="t-red">Wohlbefinden steigern und Entspannung finden</span><br>
      <span class="t-yellow">Prüfungsangst/Lernblockaden</span><span class="t-blue">Wunsch abzunehmen</span><br>
      <span class="t-blue">Schlafstörungen</span><span class="t-red">Flugangst</span><span class="t-yellow">Selbstvertrauen steigern</span><br>
      <span class="t-yellow">Lampenfieber</span><span class="t-blue">Frust</span>
    </div>

    <div class="pill pill--two">Wie Hypnose Ihr Leben verändert</div>

    <p class="copy copy--about">Hypnose ist ein Zustand tiefer Entspannung der<br>genutzt werden kann, um erwünschte Gewohnheiten<br>und Handlungsmuster zu verstärken oder<br>unerwünschte aufzulösen. Zusätzlich ist Hypnose<br>hervorragend geeignet, bei Stress oder Überforderung<br>für innere Ruhe und Wohlbefinden zu sorgen.</p>

    <svg class="back-wave" viewBox="0 0 467 220" preserveAspectRatio="none" aria-hidden="true">
      <path d="M0 18 Q240 -15 467 18 L467 220 L0 220 Z" fill="#f6b699"/>
    </svg>
    <p class="quote">Sie brauchen nicht daran zu glauben.<br>Sie brauchen es nur zulassen.<br>Sie werden begeistert sein!</p>
  </section>

</div>
</body>
</html>
```